Etiketten für selbst erzeugten Obstbrand und Liköre
Zielgruppe
Freunde und Bekannte
Aufgabenstellung
Die Etiketten kommen auf Flaschen, die selbst erzeugten Obstbrand und Liköre enthalten. Das Etikett sollte modern, ohne Schnickschnack und edel aussehen. Das Etikett sollte nur aus grafischen Elementen und Schrift bestehen (keine Bilder/Fotos). Die Schnapssorte selbst trage ich auf einem reservierten Feld handschriftlich auf dem Etikett ein. Es sollte maximal 7cm hoch und 10cm breit sein. Die Flaschen werden ausschließlich verschenkt.

```html
<!DOCTYPE html>
<html lang="de">
<head>
<meta charset="utf-8">
<title>Etikett Obstbrand – Selbst erzeugt</title>
<link rel="stylesheet" href="https://fonts.googleapis.com/css2?family=Delius&display=swap">
<style>
  :root {
    --page: #ffffff;
    --label: #e9e8ec;
    --ink: #141414;
    --pear: #8aa63a;
    --apple: #c8413a;
    --leaf: #4e9a3c;
  }
  html, body {
    margin: 0;
    padding: 0;
    overflow: hidden;
  }
  body {
    width: 1200px;
    height: 1182px;
    background: var(--page);
    position: relative;
    font-family: "Delius", cursive;
  }
  .label {
    position: absolute;
    left: 50px;
    top: 211px;
    width: 1100px;
    height: 760px;
    background: var(--label);
  }
  .divider {
    position: absolute;
    left: 64px;
    width: 962px;
    height: 40px;
  }
  .divider--top { top: 56px; }
  .divider--bottom { top: 686px; }
  .ornament {
    position: absolute;
    left: 331px;
    top: 0;
    width: 300px;
    height: 40px;
    border-radius: 20px;
    background: var(--ink);
  }
  .divider svg { position: absolute; left: 0; top: 0; }
  .pear-art {
    position: absolute;
    left: 80px;
    top: 150px;
    width: 300px;
    height: 320px;
    border-radius: 45% 45% 50% 50% / 35% 35% 65% 65%;
    background: radial-gradient(ellipse at 50% 65%, #b9c98a 0%, #dfe3cc 70%, var(--label) 100%);
  }
  .fruit-art {
    position: absolute;
    left: 800px;
    top: 315px;
    width: 245px;
    height: 342px;
    border-radius: 50% 50% 50% 50% / 40% 40% 60% 60%;
    background: radial-gradient(ellipse at 50% 62%, #e3aaa6 0%, #e9d6d8 65%, var(--label) 100%);
  }
  .product-name {
    position: absolute;
    left: 300px;
    top: 338px;
    margin: 0;
    font-size: 132px;
    font-weight: 400;
    letter-spacing: 4px;
    line-height: 1;
    color: var(--ink);
  }
  .tagline {
    position: absolute;
    left: 125px;
    top: 560px;
    margin: 0;
    font-size: 52px;
    line-height: 1;
    letter-spacing: 2px;
    color: var(--ink);
  }
</style>
</head>
<body>
  <main class="label">
    <div class="divider divider--top">
      <svg width="962" height="40" viewBox="0 0 962 40">
        <line x1="10" y1="20" x2="952" y2="20" stroke="var(--ink)" stroke-width="6"/>
        <circle cx="8" cy="20" r="8" fill="var(--ink)"/>
        <circle cx="954" cy="20" r="8" fill="var(--ink)"/>
      </svg>
      <div class="ornament" role="img" aria-label="Verschnörkeltes Zierornament in der Mitte der Linie"></div>
    </div>

    <div class="pear-art" role="img" aria-label="Linienzeichnung einer Birne mit Blatt in Grün"></div>
    <div class="fruit-art" role="img" aria-label="Linienzeichnung eines Apfels mit grünem Blatt in Rot"></div>

    <h1 class="product-name">BRAND</h1>
    <p class="tagline">Selbst erzeugt</p>

    <div class="divider divider--bottom">
      <svg width="962" height="40" viewBox="0 0 962 40">
        <line x1="10" y1="20" x2="952" y2="20" stroke="var(--ink)" stroke-width="6"/>
        <circle cx="8" cy="20" r="8" fill="var(--ink)"/>
        <circle cx="954" cy="20" r="8" fill="var(--ink)"/>
      </svg>
      <div class="ornament" role="img" aria-label="Verschnörkeltes Zierornament in der Mitte der Linie"></div>
    </div>
  </main>
</body>
</html>
```